Meadow Lark Roasters (coffee packaging design)

Project Overview:
🔥 Attention for Designer

You have been provided with detailed brand files, fonts, and reference designs for a reason. I expect work that is better than what I could create myself. The design should be thoughtful, professional, and aligned with our brand identity.

Read the full project description carefully. Every detail matters. If something is unclear, ask questions before starting. Do not just drop logos or assets onto a layout. Understand the intent and build something that fits the vision.

Rushed or mediocre work will not be accepted. I want quality over quantity with real creative thinking and brand awareness behind it.
We’re creating a high-end yet playful packaging design for Meadow Lark Roasters, intended to reflect the classy and nature-inspired feel of Pine Hollow(pinehollowyardplay.example) while adding a touch of lighthearted charm.

Design Elements to Include

Logo & Brand Cues: Incorporate the Pine Hollow logo (round circle with dog head) and use our established color palette and leafy, forestry brand patterns. This will ensure consistency and a high-end feel.

Doodle Elements (Optional): If it suits the design, feel free to incorporate the doodle-style handwriting and sketches that appear on our website (like dog names or playful notes). This adds a personal and approachable touch, though it’s not mandatory.

Bag Format: Design for a 16 oz bag, with the option to either do a full custom print or a high-quality branded sticker on a neutral bag. The goal is to make the packaging feel special and on-brand.

Overall Vibe
Think modern, classy, and a little bit whimsical. The packaging should look polished enough to be a premium product while still capturing the fun, dog-friendly personality of Pine Hollow.
Needs: its own special logo something that can be put on cups, and stickers. We also want the bag design to feel special and not just a logo slapped onto a coffee bag, so in a way i want 2 deliverables.

fonts: in the files uploaded

Target Market(s)

Dog Owners

Font styles to use
Other font styles liked:
• Fonts are in files

Requirements
Must have
• Use our brand guidelines

```html
<!DOCTYPE html>
<html lang="en">
<head>
<meta charset="utf-8">
<title>Meadow Lark Roasters – 16 oz Bag Designs</title>
<link href="https://fonts.googleapis.com/css2?family=Barlow+Condensed:wght@500;600;700&family=Patrick+Hand&display=swap" rel="stylesheet">
<style>
  :root{
    --canvas:#efe9df;
    --bag-green:#4b6a2f;
    --bag-green-dark:#3f5c27;
    --panel-green:#486629;
    --lime:#c8de3f;
    --lime-soft:rgba(200,222,63,.32);
    --cream-soft:rgba(233,220,184,.28);
    --brown-soft:rgba(110,82,52,.30);
    --rule:#b9d13a;
  }
  *{box-sizing:border-box;margin:0;padding:0}
  html,body{width:1200px;height:1178px;overflow:hidden;background:var(--canvas)}
  .canvas{position:relative;width:1200px;height:1178px}

  .bag{position:absolute;top:140px;width:420px;height:900px;background:var(--bag-green);border-radius:6px 6px 4px 4px;overflow:hidden}
  .bag--scatter{left:90px}
  .bag--framed{left:690px}

  .seal{position:absolute;left:0;top:0;width:100%;height:34px;background:var(--bag-green-dark)}
  .seal svg{display:block}

  .pattern-field{position:absolute;left:0;top:34px;width:100%;height:866px}
  .bag--scatter .pattern-field{
    background:
      radial-gradient(circle at 18% 12%,var(--lime-soft) 0,transparent 60px),
      radial-gradient(circle at 78% 18%,var(--cream-soft) 0,transparent 70px),
      radial-gradient(circle at 50% 30%,var(--lime-soft) 0,transparent 60px),
      radial-gradient(circle at 10% 55%,var(--cream-soft) 0,transparent 55px),
      radial-gradient(circle at 90% 60%,var(--lime-soft) 0,transparent 55px),
      radial-gradient(circle at 22% 88%,var(--lime-soft) 0,transparent 65px),
      radial-gradient(circle at 80% 92%,var(--cream-soft) 0,transparent 65px),
      var(--bag-green);
  }
  .bag--framed .pattern-field{
    background:
      radial-gradient(circle at 15% 10%,var(--lime-soft) 0,transparent 80px),
      radial-gradient(circle at 50% 14%,var(--cream-soft) 0,transparent 90px),
      radial-gradient(circle at 85% 10%,var(--lime-soft) 0,transparent 80px),
      radial-gradient(circle at 30% 28%,var(--brown-soft) 0,transparent 80px),
      radial-gradient(circle at 72% 28%,var(--lime-soft) 0,transparent 80px),
      radial-gradient(circle at 4% 60%,var(--lime-soft) 0,transparent 60px),
      radial-gradient(circle at 96% 60%,var(--cream-soft) 0,transparent 60px),
      radial-gradient(circle at 50% 98%,var(--lime-soft) 0,transparent 80px),
      linear-gradient(180deg,#5e8136 0%,#587a31 50%,#56772f 100%);
  }

  .panel{position:absolute;left:42px;top:250px;width:336px;height:565px;background:var(--panel-green);border:2px solid var(--lime)}

  .content{position:absolute;left:0;width:100%;display:flex;flex-direction:column;align-items:center;text-align:center;color:var(--lime)}
  .bag--scatter .content{top:230px}
  .panel .content{top:40px}

  .mark{width:92px;height:92px;border-radius:50%;background:var(--lime);margin-bottom:26px}
  .panel .mark{width:84px;height:84px;margin-bottom:20px}

  .brand-name{font-family:"Barlow Condensed",sans-serif;font-weight:700;font-size:46px;line-height:1;letter-spacing:1px;text-transform:uppercase;color:var(--lime)}
  .tagline{font-family:"Patrick Hand",cursive;font-size:30px;line-height:1.2;color:var(--lime)}
  .rule{width:270px;height:2px;background:var(--rule);opacity:.8}
  .claim{font-family:"Barlow Condensed",sans-serif;font-weight:600;font-size:29px;line-height:1.1;text-transform:uppercase;color:var(--lime);padding:14px 0}
  .net-weight{font-family:"Barlow Condensed",sans-serif;font-weight:600;font-size:28px;line-height:1.2;color:var(--lime)}

  .bag--scatter .tagline{margin-top:80px}
  .bag--scatter .tagline + .rule{margin-top:55px}
  .bag--scatter .net-weight{margin-top:55px}

  .panel .tagline{margin-top:34px}
  .panel .tagline + .rule{margin-top:32px}
  .panel .net-weight{margin-top:30px}
</style>
</head>
<body>
<main class="canvas">

  <section class="bag bag--scatter" aria-label="Bag design with scattered motifs">
    <div class="pattern-field" role="img" aria-label="Scattered leaf, sprig and doodle motifs in lime and cream over green"></div>
    <div class="seal">
      <svg width="420" height="34" viewBox="0 0 420 34">
        <g stroke="#587a37" stroke-width="2">
          <line x1="40" y1="10" x2="130" y2="10"/><line x1="40" y1="17" x2="130" y2="17"/><line x1="40" y1="24" x2="130" y2="24"/>
          <line x1="290" y1="10" x2="380" y2="10"/><line x1="290" y1="17" x2="380" y2="17"/><line x1="290" y1="24" x2="380" y2="24"/>
        </g>
      </svg>
    </div>
    <div class="content">
      <div class="mark"></div>
      <h1 class="brand-name">Meadow Lark<br>Roasters</h1>
      <p class="tagline">Crafted for Dog Lover</p>
      <div class="rule"></div>
      <p class="claim">Brewed for<br>Dogs Best Friends</p>
      <div class="rule"></div>
      <p class="net-weight">Net WT. 16 OZ</p>
    </div>
  </section>

  <section class="bag bag--framed" aria-label="Bag design with framed label">
    <div class="pattern-field" role="img" aria-label="All-over leafy forest pattern in lime, cream and brown on green"></div>
    <div class="seal"></div>
    <div class="panel">
      <div class="content">
        <div class="mark"></div>
        <h2 class="brand-name">Meadow Lark<br>Roasters</h2>
        <p class="tagline">Crafted for Dog Lover</p>
        <div class="rule"></div>
        <p class="claim">Brewed for<br>Dogs Best Friends</p>
        <div class="rule"></div>
        <p class="net-weight">Net WT. 16 OZ</p>
      </div>
    </div>
  </section>

</main>
</body>
</html>
```